Get Up to $ 500,000 in Business Capital within 48 hours

design a flyer offering business capital to businesses. The flyer is going to be mailed to business owners and the flyer needs to immediately capture their attention.
The flyer needs to be bold and professional and really stand-out.
pppppppppppppppppppppppppppppppppppppppppppppppppppppppppppppppppppppppppppppppppppppppppppppppppppppppppppppppppppppppppppppppppppppppppppppppppppppppppppppppppppppppppppppppppppppppppppppppppppppppppppppppppppppppppppppppppppppp

Target Market(s)

business owners

Font styles to use
Serif

Requirements
Must have
• Apply online in minutes at PellarCapital.example or call 800-GRAB-NOW
Nice to have
• We fund almost every business type. Not a business loan, receive a cash advance on your future sales.

```html
<!DOCTYPE html>
<html lang="en">
<head>
<meta charset="utf-8">
<title>Pellar Capital – Business Capital Flyer</title>
<link rel="stylesheet" href="https://fonts.googleapis.com/css2?family=Oswald:wght@300;400;500;600;700&display=swap">
<style>
  :root {
    --navy: #1c2a7a;
    --navy-deep: #0b1033;
    --sky: #1fa9e6;
    --paper: #ffffff;
    --mist: #eef2f6;
    --rule: #d5dbe3;
    --photo-light: #e8edf2;
    --photo-mid: #b9c6d6;
    --photo-dark: #2a3448;
    --note-tone: #c9cdc4;
  }
  html, body {
    margin: 0;
    padding: 0;
    width: 969px;
    height: 1200px;
    overflow: hidden;
    background: var(--paper);
  }
  .flyer { display: block; width: 969px; height: 1200px; }
  .type { font-family: 'Oswald', sans-serif; }
  .brand-name { font-weight: 500; fill: var(--navy); }
  .headline-small { font-weight: 500; fill: var(--paper); }
  .headline-large { font-weight: 700; fill: var(--paper); }
  .offer-lead { font-weight: 300; fill: var(--navy); }
  .offer-amount { font-weight: 700; fill: var(--sky); }
  .offer-accent { font-weight: 700; fill: var(--sky); }
  .feature-text { font-weight: 600; fill: var(--navy); }
  .loan-note { font-weight: 600; fill: var(--sky); }
  .advance-note { font-weight: 400; fill: var(--navy); }
  .band-text { font-weight: 500; fill: var(--paper); }
  .contact-text { font-weight: 400; fill: var(--navy); }
  .contact-link { font-weight: 500; fill: var(--sky); }
</style>
</head>
<body>
<svg class="flyer" viewBox="0 0 969 1200" xmlns="http://www.w3.org/2000/svg">
  <defs>
    <linearGradient id="photoTone" x1="0" y1="0" x2="1" y2="0.4">
      <stop offset="0" stop-color="var(--photo-light)"/>
      <stop offset="0.45" stop-color="var(--photo-light)"/>
      <stop offset="0.75" stop-color="var(--photo-mid)"/>
      <stop offset="1" stop-color="var(--photo-dark)"/>
    </linearGradient>
    <radialGradient id="noteGlow" cx="0.5" cy="0.45" r="0.5">
      <stop offset="0" stop-color="var(--note-tone)" stop-opacity="0.9"/>
      <stop offset="0.6" stop-color="var(--note-tone)" stop-opacity="0.45"/>
      <stop offset="1" stop-color="var(--note-tone)" stop-opacity="0"/>
    </radialGradient>
    <linearGradient id="headlineBanner" x1="0" y1="1" x2="0.6" y2="0">
      <stop offset="0" stop-color="#1f8fd6"/>
      <stop offset="0.45" stop-color="#1b3f96"/>
      <stop offset="1" stop-color="var(--navy-deep)"/>
    </linearGradient>
    <linearGradient id="fundBand" x1="0" y1="0" x2="1" y2="0">
      <stop offset="0" stop-color="var(--sky)"/>
      <stop offset="0.5" stop-color="#1e56a8"/>
      <stop offset="1" stop-color="var(--navy)"/>
    </linearGradient>
  </defs>

  <!-- Hero photo area -->
  <rect class="hero-photo" x="0" y="0" width="969" height="585" fill="url(#photoTone)"
        role="img" aria-label="Photo of two smiling business professionals looking at a tablet in a bright office"/>

  <!-- Brand -->
  <circle class="brand-dot" cx="229" cy="105" r="56" fill="var(--navy)"/>
  <text class="type brand-name" x="64" y="226" font-size="52" textLength="331" lengthAdjust="spacingAndGlyphs">PELLAR CAPITAL</text>

  <!-- Banknote illustration area -->
  <rect class="money-illustration" x="30" y="320" width="430" height="380" fill="url(#noteGlow)"
        role="img" aria-label="Illustration of a paper plane folded from a banknote"/>

  <!-- Headline banner -->
  <polygon class="headline-banner" points="438,393 969,393 969,585 355,585" fill="url(#headlineBanner)"/>
  <text class="type headline-small" x="457" y="459" font-size="60" textLength="360" lengthAdjust="spacingAndGlyphs">NEED BUSINESS</text>
  <text class="type headline-large" x="455" y="568" font-size="124" textLength="462" lengthAdjust="spacingAndGlyphs">CAPITAL?</text>

  <!-- Offer -->
  <text class="type offer-lead" x="889" y="650" font-size="38" text-anchor="end" textLength="375" lengthAdjust="spacingAndGlyphs">YOU CAN QUALIFY FOR UP TO</text>
  <text class="type offer-amount" x="891" y="718" font-size="72" text-anchor="end" textLength="272" lengthAdjust="spacingAndGlyphs">$500,000</text>
  <text class="type" x="897" y="773" font-size="52" text-anchor="end" textLength="361" lengthAdjust="spacingAndGlyphs"><tspan class="offer-lead">IN JUST </tspan><tspan class="offer-accent">24 HOURS</tspan></text>

  <!-- Features -->
  <g class="feature feature-credit">
    <circle cx="204" cy="860" r="46" fill="var(--mist)" stroke="var(--rule)" stroke-width="1"/>
    <path d="M160,872 A46,46 0 0 0 248,872" fill="none" stroke="var(--sky)" stroke-width="4"/>
    <path d="M180,870 A26,26 0 0 1 230,858" fill="none" stroke="var(--sky)" stroke-width="6"/>
    <circle cx="206" cy="866" r="11" fill="none" stroke="var(--navy)" stroke-width="4"/>
    <line x1="206" y1="866" x2="186" y2="848" stroke="var(--navy)" stroke-width="4" stroke-linecap="round"/>
  </g>
  <text class="type feature-text" x="274" y="858" font-size="33">No minimum</text>
  <text class="type feature-text" x="274" y="896" font-size="33">Credit score</text>

  <line class="feature-divider" x1="478" y1="823" x2="478" y2="905" stroke="var(--rule)" stroke-width="1.5"/>

  <g class="feature feature-application">
    <circle cx="566" cy="860" r="46" fill="var(--mist)" stroke="var(--rule)" stroke-width="1"/>
    <path d="M522,872 A46,46 0 0 0 610,872" fill="none" stroke="var(--sky)" stroke-width="4"/>
    <path d="M550,833 h22 l10,10 v34 h-32 z" fill="var(--paper)" stroke="var(--navy)" stroke-width="2.5" stroke-linejoin="round"/>
    <line x1="556" y1="850" x2="574" y2="850" stroke="var(--sky)" stroke-width="2.5"/>
    <line x1="556" y1="858" x2="576" y2="858" stroke="var(--sky)" stroke-width="2.5"/>
    <line x1="556" y1="866" x2="568" y2="866" stroke="var(--sky)" stroke-width="2.5"/>
    <circle cx="581" cy="872" r="8" fill="var(--paper)" stroke="var(--navy)" stroke-width="2"/>
    <path d="M577,872 l3,3 l5,-6" fill="none" stroke="var(--sky)" stroke-width="2"/>
  </g>
  <text class="type feature-text" x="633" y="858" font-size="33">Simple 1 page</text>
  <text class="type feature-text" x="633" y="896" font-size="33">application</text>

  <!-- Product notes -->
  <text class="type loan-note" x="484" y="989" font-size="48" text-anchor="middle" textLength="400" lengthAdjust="spacingAndGlyphs">NOT A BUSINESS LOAN</text>
  <text class="type advance-note" x="485" y="1040" font-size="40" text-anchor="middle" textLength="772" lengthAdjust="spacingAndGlyphs">GET A CASH ADVANCE TODAY ON YOUR FUTURE SALES.</text>

  <!-- Funding band -->
  <rect class="fund-band" x="0" y="1063" width="969" height="59" fill="url(#fundBand)"/>
  <text class="type band-text" x="481" y="1107" font-size="40" text-anchor="middle" textLength="672" lengthAdjust="spacingAndGlyphs">WE FUND VIRTUALLY EVERY TYPE OF BUSINESS</text>

  <!-- Contact -->
  <text class="type" x="485" y="1170" font-size="34" text-anchor="middle" textLength="888" lengthAdjust="spacingAndGlyphs"><tspan class="contact-text">Apply in minutes at </tspan><tspan class="contact-link">PellarCapital.example</tspan><tspan class="contact-text"> or Call </tspan><tspan class="contact-link">1-800-GRAB-NOW</tspan></text>
</svg>
</body>
</html>
```